5-star Hotel Web Design Project

I need a custom website design for a 5-star hotel. For full details please look at the attached ZIP archive.

The design should be in layers in Photoshop/Illustrator/InDesign format with all the icons/shapes/maps/graphic assets in vector format (svg, ai, eps) as much as possible.

I prefer white, simple but elegant websites. Please consider the performance/coding experience. We're not making something to show off our design skills on a design contest with fancy parallax effects and confusing animations. We're trying to create usable, functional and clean UI with good UX.

I would like to receive a few option for the color scheme to choose from.

The website will be custom coded, i.e. I'm not using WordPress.

NOTE: Don't bother to submit the generic WordPress style templates. We're looking for something custom made with attention to details. That's why the price is not guaranteed, but don't be mistaken, I'm a long time buyer here on FolioBazaar and all my projects are paid in full.
Updates

Low design quality

Target Market(s)

Europe

Industry/Entity Type

Hotel

Number of Pages Required

5+ page

```html
<!DOCTYPE html>
<html lang="en">
<head>
<meta charset="utf-8">
<title>Amberline Resort – Home</title>
<link rel="stylesheet" href="https://fonts.googleapis.com/css2?family=Tinos:wght@400;700&family=Lato:wght@400;700&display=swap">
<style>
:root{
  --brand:#990a35;
  --brand-dark:#7d0629;
  --ink:#222;
  --muted:#555;
  --line:#e4e4e4;
  --panel:#f3f3f3;
  --white:#fff;
  --footer:#0b0b0b;
  --gold:#e0a800;
}
*{box-sizing:border-box;margin:0;padding:0}
html,body{width:1200px;height:5000px;overflow:hidden;background:var(--white)}
body{position:relative;font-family:"Lato",sans-serif;color:var(--ink)}
.abs{position:absolute}
.serif{font-family:"Tinos",serif}
.btn{position:absolute;display:flex;align-items:center;justify-content:center;gap:8px;background:var(--brand);color:var(--white);font-weight:700;font-size:15px;border-radius:24px}
.btn svg{width:14px;height:14px}
.photo{position:absolute}

/* header */
.site-header{position:absolute;left:0;top:0;width:1200px;height:93px;background:var(--white);border-bottom:1px solid var(--line)}
.brand-name{position:absolute;font-family:"Tinos",serif;color:var(--brand);font-weight:400}
.brand-mark{position:absolute;border-radius:50%;background:var(--brand)}
.top-phone{position:absolute;left:652px;top:14px;display:flex;align-items:center;gap:10px;color:var(--brand);font-weight:700;font-size:17px}
.top-phone .dot{width:28px;height:28px;border-radius:50%;background:var(--brand);display:flex;align-items:center;justify-content:center}
.contact-btn{left:845px;top:12px;width:136px;height:32px;font-weight:400;font-size:16px}
.lang{position:absolute;left:1003px;top:18px;font-size:14px;display:flex;align-items:center;gap:6px}
.main-nav{position:absolute;right:110px;top:62px;display:flex;font-size:16px;font-weight:700;gap:0}
.main-nav span{padding:0 24px;border-left:2px solid var(--ink);line-height:14px}
.main-nav span:first-child{border:none;color:var(--brand)}
.main-nav span:last-child{padding-right:0}

/* hero */
.hero{position:absolute;left:0;top:93px;width:1200px;height:609px;background:linear-gradient(160deg,#5f8c93 0%,#8fb0ae 22%,#c9c3b4 45%,#d8d0c2 62%,#6a8fa6 80%,#4a7fa0 100%)}
.hero-shade{position:absolute;inset:0;background:linear-gradient(90deg,rgba(0,0,0,.35),rgba(0,0,0,0) 60%)}
.hero-title{position:absolute;left:112px;top:220px;font-family:"Tinos",serif;font-weight:700;color:var(--white);font-size:33px;line-height:41px}
.booking{position:absolute;left:112px;top:327px;width:520px;height:48px;background:var(--white);border-radius:26px}
.booking .field{position:absolute;top:15px;font-size:14px;color:#444;display:flex;gap:6px;align-items:center}
.booking .sep{position:absolute;left:132px;top:12px;width:1px;height:24px;background:#ccc}
.booking .btn{left:323px;top:0;width:197px;height:48px;font-size:16px}
.hero-arrow{position:absolute;top:290px}
.dots{position:absolute;left:560px;top:557px;display:flex;gap:8px}
.dots i{width:12px;height:12px;border-radius:50%;background:rgba(255,255,255,.55)}
.dots i:first-child{background:var(--white)}

/* glance */
.section-title{position:absolute;width:1200px;left:0;text-align:center;font-family:"Tinos",serif;font-weight:700;font-size:40px}
.glance-title{position:absolute;left:648px;top:790px;font-family:"Tinos",serif;font-weight:700;font-size:38px}
.glance-text{position:absolute;left:648px;top:840px;width:440px;font-size:13.5px;line-height:28px;color:var(--muted)}
.badge{position:absolute;top:970px;width:100px;height:100px;border-radius:50%;background:#ececec;border:3px solid #ddd;box-shadow:0 2px 6px rgba(0,0,0,.2)}

/* offers */
.offers{position:absolute;left:0;top:1235px;width:1200px;height:1455px;background:var(--panel)}
.offer{position:absolute;width:315px}
.offer .pic{position:absolute;left:0;top:0;width:315px;height:236px}
.offer .band{position:absolute;left:0;top:190px;width:315px;height:46px;background:var(--brand);color:var(--white);font-family:"Tinos",serif;font-size:20px;padding:11px 0 0 17px}
.offer p{position:absolute;left:0;top:252px;width:315px;font-size:12.5px;line-height:26px;color:var(--muted)}
.offer .price{position:absolute;left:0;top:308px;font-size:18px;color:var(--ink)}
.offer .btn{left:0;top:345px;width:158px;height:42px}

/* testimonials */
.testi-pic{position:absolute;left:0;top:2690px;width:600px;height:390px;background:linear-gradient(135deg,#1b1d4d,#3b3d8a 45%,#13153a 80%)}
.testi{position:absolute;left:600px;top:2690px;width:600px;height:390px;background:var(--brand);color:var(--white)}
.testi h2{position:absolute;left:72px;top:75px;font-family:"Tinos",serif;font-size:38px;font-weight:700}
.testi p{position:absolute;left:72px;top:125px;width:430px;font-style:italic;font-size:15px;line-height:29px}
.avatar{position:absolute;left:75px;top:253px;width:42px;height:42px;border-radius:50%;background:#c9c1bb;border:2px solid var(--white)}
.stars{position:absolute;left:128px;top:252px;color:var(--gold);font-size:16px;letter-spacing:1px}
.testi .name{position:absolute;left:128px;top:272px;font-size:19px;font-weight:700}
.tbtn{position:absolute;top:268px;width:34px;height:34px;border:1px solid var(--white)}

/* benefits */
.benefit{position:absolute;width:233px;height:205px;background:var(--white);box-shadow:0 2px 10px rgba(0,0,0,.12);text-align:center}
.benefit .icon{position:absolute;left:86px;top:22px;width:62px;height:62px;border:2px solid var(--brand);border-radius:10px;background:#fbeef2}
.benefit h3{position:absolute;left:0;top:104px;width:233px;font-family:"Tinos",serif;font-weight:400;font-size:17px;line-height:20px}
.benefit p{position:absolute;left:14px;top:130px;width:205px;font-size:12.5px;line-height:21px;color:var(--muted)}
.benefit.tall h3{top:95px}
.benefit.tall p{top:138px}

/* newsletter */
.newsletter{position:absolute;left:0;top:3805px;width:1200px;height:340px;background:linear-gradient(120deg,var(--brand-dark),var(--brand) 50%,#8a0830)}
.newsletter h2{position:absolute;left:0;top:85px;width:1200px;text-align:center;font-family:"Tinos",serif;font-size:40px;color:var(--white)}
.newsletter p{position:absolute;left:270px;top:135px;width:660px;text-align:center;font-size:17px;line-height:29px;color:var(--white)}
.subscribe{position:absolute;left:340px;top:208px;width:520px;height:50px;background:var(--white);border-radius:26px;border:2px solid var(--white)}
.subscribe span{position:absolute;left:26px;top:15px;font-size:13px;color:#444}
.subscribe .btn{left:343px;top:0;width:173px;height:46px;font-size:16px}

/* accommodation */
.room{position:absolute;top:4285px;width:240px}
.room .pic{position:absolute;left:0;top:0;width:240px;height:160px}
.room h3{position:absolute;left:0;top:176px;font-family:"Tinos",serif;font-size:21px;font-weight:700}
.room p{position:absolute;left:0;top:206px;width:240px;font-size:12.5px;line-height:24px;color:var(--muted)}
.room .rate{position:absolute;left:0;top:258px;font-size:14px;font-weight:700}
.room .more{position:absolute;left:0;top:290px;font-size:15px;font-weight:700;color:var(--brand);text-decoration:underline;display:flex;gap:6px;align-items:center}
.slide-arrow{position:absolute;top:4435px}

/* footer */
.site-footer{position:absolute;left:0;top:4680px;width:1200px;height:320px;background:var(--footer);color:var(--white)}
.fcol{position:absolute;top:80px;font-size:15px;line-height:29px}
.fcol h4{font-size:16px;font-weight:700;margin-bottom:4px}
.fcontact div{display:flex;gap:10px;align-items:flex-start}
.frule{position:absolute;left:112px;top:255px;width:976px;height:1px;background:#444}
.copy{position:absolute;left:112px;top:280px;font-size:13px}
.social{position:absolute;top:273px;width:28px;height:28px;border-radius:50%;background:var(--white)}
</style>
</head>
<body>

<header class="site-header">
  <div class="brand-mark" style="left:134px;top:10px;width:14px;height:14px"></div>
  <div class="brand-name" style="left:108px;top:32px;font-size:24px">Amberline Resort</div>
  <div class="top-phone"><span class="dot"><svg width="14" height="14" viewBox="0 0 24 24" fill="#fff"><path d="M6.6 10.8a15 15 0 0 0 6.6 6.6l2.2-2.2a1 1 0 0 1 1-.25 11.4 11.4 0 0 0 3.6.57 1 1 0 0 1 1 1V20a1 1 0 0 1-1 1A17 17 0 0 1 3 4a1 1 0 0 1 1-1h3.5a1 1 0 0 1 1 1c0 1.25.2 2.45.57 3.6a1 1 0 0 1-.25 1z"/></svg></span>888 - 888 - 8888</div>
  <div class="btn contact-btn">CONTACT</div>
  <div class="lang"><svg width="14" height="14" viewBox="0 0 24 24" fill="none" stroke="#333" stroke-width="2"><circle cx="12" cy="12" r="10"/><path d="M2 12h20M12 2c3 3 3 17 0 20M12 2c-3 3-3 17 0 20"/></svg>English <svg width="10" height="10" viewBox="0 0 10 10"><path d="M1 3l4 4 4-4" stroke="#333" fill="none" stroke-width="1.5"/></svg></div>
  <nav class="main-nav"><span>Home</span><span>Amberline Resort</span><span>Book direct</span><span>Special Offers</span><span>Location</span></nav>
</header>

<section class="hero" role="img" aria-label="Aerial view of the seaside resort with pools and beach">
  <div class="hero-shade"></div>
  <div class="hero-title">Book direct with 20% discount<br>Price from XX per night</div>
  <div class="booking">
    <div class="field" style="left:24px">&#9638; Check In &#8964;</div>
    <div class="sep"></div>
    <div class="field" style="left:160px">&#9638; Check Out &#8964;</div>
    <div class="btn">Check Availability</div>
  </div>
  <svg class="hero-arrow" style="left:62px" width="20" height="36" viewBox="0 0 20 36"><path d="M18 2L2 18l16 16" stroke="#fff" stroke-width="2" fill="none"/></svg>
  <svg class="hero-arrow" style="left:1110px" width="20" height="36" viewBox="0 0 20 36"><path d="M2 2l16 16L2 34" stroke="#fff" stroke-width="2" fill="none"/></svg>
  <div class="dots"><i></i><i></i><i></i><i></i></div>
</section>

<section class="glance">
  <div class="photo" role="img" aria-label="Guest relaxing on a sailing boat with the resort skyline behind" style="left:112px;top:786px;width:458px;height:364px;background:linear-gradient(180deg,#8fb7dd 0%,#b9d2ea 45%,#3f6f95 60%,#c9b9aa 80%,#8d7b70 100%)"></div>
  <h2 class="glance-title">At A Glance</h2>
  <p class="glance-text">Lorem ipsum dolor sit amet, consectetur adipiscing elit,d do eiusmod tempor incididunt ut labore et dolore &nbsp;aliqua. Quis ipsum suspendisse ultrices gravida. Risus commodo viverra Lorem ipsum dolor sit amet, consectetur adipiscing elit,d do eiusmod tempor</p>
  <div class="badge" style="left:638px"></div>
  <div class="badge" style="left:755px;background:#14a06a;border-color:#0e8a59"></div>
  <div class="badge" style="left:872px;background:#e6ddd4"></div>
  <div class="badge" style="left:989px;background:#eedfd8"></div>
  <div class="btn" style="left:648px;top:1093px;width:158px;height:44px">Learn more <svg viewBox="0 0 16 16"><circle cx="8" cy="8" r="8" fill="#fff"/><path d="M6.5 4.5L10 8l-3.5 3.5" stroke="#990a35" stroke-width="2" fill="none"/></svg></div>
</section>

<section class="offers">
  <h2 class="section-title" style="top:75px;font-size:38px">Special Offers</h2>

  <div class="offer" style="left:112px;top:155px">
    <div class="pic" role="img" aria-label="Resort lit up at night" style="background:linear-gradient(180deg,#0a0a12,#3a2a14 60%,#234018)"></div>
    <div class="band">Easter Offer</div>
    <p>Lorem ipsum dolor sit amet, consectetur adipiscing elit, sed do eiusmod tempor incididunt</p>
    <div class="price">Price from XX per night</div>
    <div class="btn">Book Now <svg viewBox="0 0 16 16"><circle cx="8" cy="8" r="8" fill="#fff"/><path d="M6.5 4.5L10 8l-3.5 3.5" stroke="#990a35" stroke-width="2" fill="none"/></svg></div>
  </div>
  <div class="offer" style="left:443px;top:155px">
    <div class="pic" role="img" aria-label="Ballroom with chandeliers" style="background:linear-gradient(180deg,#6b4a22,#c9a36a 45%,#5a3a1e)"></div>
    <div class="band">Summer Offer</div>
    <p>Lorem ipsum dolor sit amet, consectetur adipiscing elit, sed do eiusmod tempor incididunt</p>
    <div class="price">Price from XX per night</div>
    <div class="btn">Book Now <svg viewBox="0 0 16 16"><circle cx="8" cy="8" r="8" fill="#fff"/><path d="M6.5 4.5L10 8l-3.5 3.5" stroke="#990a35" stroke-width="2" fill="none"/></svg></div>
  </div>
  <div class="offer" style="left:774px;top:155px">
    <div class="pic" role="img" aria-label="Guest room with table and floral bedspread" style="background:linear-gradient(180deg,#b9a58f,#8a6a4d 50%,#d9c4c4)"></div>
    <div class="band">Early Bookings 2021</div>
    <p>Lorem ipsum dolor sit amet, consectetur adipiscing elit, sed do eiusmod tempor incididunt</p>
    <div class="price">Price from XX per night</div>
    <div class="btn">Book Now <svg viewBox="0 0 16 16"><circle cx="8" cy="8" r="8" fill="#fff"/><path d="M6.5 4.5L10 8l-3.5 3.5" stroke="#990a35" stroke-width="2" fill="none"/></svg></div>
  </div>

  <div class="offer" style="left:112px;top:568px">
    <div class="pic" role="img" aria-label="Banquet hall set for New Year" style="background:linear-gradient(180deg,#6a3a1e,#c99a5a 50%,#7a4a2a)"></div>
    <div class="band">New Year Offer</div>
    <p>Lorem ipsum dolor sit amet, consectetur adipiscing elit, sed do eiusmod tempor incididunt</p>
    <div class="price">Price from XX per night</div>
    <div class="btn">Book Now <svg viewBox="0 0 16 16"><circle cx="8" cy="8" r="8" fill="#fff"/><path d="M6.5 4.5L10 8l-3.5 3.5" stroke="#990a35" stroke-width="2" fill="none"/></svg></div>
  </div>
  <div class="offer" style="left:443px;top:568px">
    <div class="pic" role="img" aria-label="Snow covered resort grounds" style="background:linear-gradient(180deg,#4a4f55,#a7adb2 50%,#d6d9dc)"></div>
    <div class="band">Christmas Offer</div>
    <p>Lorem ipsum dolor sit amet, consectetur adipiscing elit, sed do eiusmod tempor incididunt</p>
    <div class="price">Price from XX per night</div>
    <div class="btn">Book Now <svg viewBox="0 0 16 16"><circle cx="8" cy="8" r="8" fill="#fff"/><path d="M6.5 4.5L10 8l-3.5 3.5" stroke="#990a35" stroke-width="2" fill="none"/></svg></div>
  </div>
  <div class="offer" style="left:774px;top:568px">
    <div class="pic" role="img" aria-label="Garden terrace by the sea" style="background:linear-gradient(180deg,#7fa3c7,#a8b5b0 45%,#5f8a4e 75%,#8a6a5a)"></div>
    <div class="band">Special Offer -50%</div>
    <p>Lorem ipsum dolor sit amet, consectetur adipiscing elit, sed do eiusmod tempor incididunt</p>
    <div class="price">Price from XX per night</div>
    <div class="btn">Book Now <svg viewBox="0 0 16 16"><circle cx="8" cy="8" r="8" fill="#fff"/><path d="M6.5 4.5L10 8l-3.5 3.5" stroke="#990a35" stroke-width="2" fill="none"/></svg></div>
  </div>

  <div class="offer" style="left:112px;top:978px">
    <div class="pic" role="img" aria-label="Lounge with fireplace and popcorn" style="background:linear-gradient(180deg,#2a1a10,#6a3a18 50%,#1a120c)"></div>
    <div class="band">Weekend Offer</div>
    <p>Lorem ipsum dolor sit amet, consectetur adipiscing elit, sed do eiusmod tempor incididunt</p>
    <div class="price">Price from XX per night</div>
    <div class="btn">Book Now <svg viewBox="0 0 16 16"><circle cx="8" cy="8" r="8" fill="#fff"/><path d="M6.5 4.5L10 8l-3.5 3.5" stroke="#990a35" stroke-width="2" fill="none"/></svg></div>
  </div>
  <div class="offer" style="left:443px;top:978px">
    <div class="pic" role="img" aria-label="Indoor pool under warm lighting" style="background:linear-gradient(180deg,#7a4a1a,#d09a4a 45%,#2f6f7a)"></div>
    <div class="band">May Specials</div>
    <p>Lorem ipsum dolor sit amet, consectetur adipiscing elit, sed do eiusmod tempor incididunt</p>
    <div class="price">Price from XX per night</div>
    <div class="btn">Book Now <svg viewBox="0 0 16 16"><circle cx="8" cy="8" r="8" fill="#fff"/><path d="M6.5 4.5L10 8l-3.5 3.5" stroke="#990a35" stroke-width="2" fill="none"/></svg></div>
  </div>
  <div class="offer" style="left:774px;top:978px">
    <div class="pic" role="img" aria-label="Resort building with balconies" style="background:linear-gradient(180deg,#9fc1e4,#d9cdb8 50%,#6f8a5a)"></div>
    <div class="band">Long Weekend in September</div>
    <p>Lorem ipsum dolor sit amet, consectetur adipiscing elit, sed do eiusmod tempor incididunt</p>
    <div class="price">Price from XX per night</div>
    <div class="btn">Book Now <svg viewBox="0 0 16 16"><circle cx="8" cy="8" r="8" fill="#fff"/><path d="M6.5 4.5L10 8l-3.5 3.5" stroke="#990a35" stroke-width="2" fill="none"/></svg></div>
  </div>
</section>

<div class="testi-pic" role="img" aria-label="Guests at the resort bowling center"></div>
<section class="testi">
  <h2>Testimonials</h2>
  <p>Lorem ipsum dolor sit amet, consectetur adipiscing elit, sed do eiusmod tempor incididunt ut labore et dolore a aliqua. Quis ipsum susse ultrices gravida. Risus commodo viverra nas accumsan lacus vel facilisis.</p>
  <div class="avatar" role="img" aria-label="Guest portrait"></div>
  <div class="stars">&#9733;&#9733;&#9733;&#9733;&#9733;</div>
  <div class="name">John Doe</div>
  <div class="tbtn" style="left:406px"><svg width="32" height="32" viewBox="0 0 32 32"><path d="M19 9l-7 7 7 7" stroke="#fff" stroke-width="1.8" fill="none"/></svg></div>
  <div class="tbtn" style="left:448px"><svg width="32" height="32" viewBox="0 0 32 32"><path d="M13 9l7 7-7 7" stroke="#fff" stroke-width="1.8" fill="none"/></svg></div>
</section>

<section class="benefits">
  <h2 class="section-title" style="top:3150px;font-size:38px">Our Benefits</h2>
  <div class="benefit" style="left:105px;top:3215px"><div class="icon" role="img" aria-label="Sun over the sea icon"></div><h3>First line to the sea</h3><p>with direct access to the South beach in Marevo</p></div>
  <div class="benefit" style="left:357px;top:3215px"><div class="icon" role="img" aria-label="Water slide icon"></div><h3>Aquapark</h3><p>32 fun water slides, 2 of which 150m long</p></div>
  <div class="benefit" style="left:609px;top:3215px"><div class="icon" role="img" aria-label="Room with lamp icon"></div><h3>Luxurious rooms</h3><p>Spacious open-air terraces and provide stunning views...</p></div>
  <div class="benefit tall" style="left:861px;top:3215px"><div class="icon" role="img" aria-label="Fork and spoon icon"></div><h3>International restaurants<br>&amp; bars</h3><p>4 international a-la-cart restaurants and 5 main buffet</p></div>
  <div class="benefit" style="left:105px;top:3440px"><div class="icon" role="img" aria-label="Meditation icon"></div><h3>Relax and Wellness center</h3><p>Plenty of options to boost your physical and mental energy...</p></div>
  <div class="benefit" style="left:357px;top:3440px"><div class="icon" role="img" aria-label="Dumbbell icon"></div><h3>Fitness Center</h3><p>Enhance your physical condition!</p></div>
  <div class="benefit" style="left:609px;top:3440px"><div class="icon" role="img" aria-label="Bowling pins icon"></div><h3>Bowling Center</h3><p>Spend your leisure time in Amberline Resort's Bowling Center..</p></div>
  <div class="benefit" style="left:861px;top:3440px"><div class="icon" role="img" aria-label="Children icon"></div><h3>Kids club</h3><p>The children's club offers a variety of activities for all our young...</p></div>
  <div class="btn" style="left:494px;top:3680px;width:212px;height:44px">View All Benefits <svg viewBox="0 0 16 16"><circle cx="8" cy="8" r="8" fill="#fff"/><path d="M6.5 4.5L10 8l-3.5 3.5" stroke="#990a35" stroke-width="2" fill="none"/></svg></div>
</section>

<section class="newsletter">
  <h2>Subscribe to Amberline Resort Newsletter</h2>
  <p>Lorem ipsum dolor sit amet, consectetur adipiscing elit, sed do eiusmod tempor incididunt ut labore et dolore magna aliqua.</p>
  <div class="subscribe"><span>Enter Your Email Address</span><div class="btn">Subscribe me</div></div>
</section>

<section class="accommodation">
  <h2 class="section-title" style="top:4220px;font-size:38px">Accommodation</h2>
  <svg class="slide-arrow" style="left:60px" width="18" height="32" viewBox="0 0 18 32"><path d="M16 2L2 16l14 14" stroke="#333" stroke-width="1.6" fill="none"/></svg>
  <svg class="slide-arrow" style="left:1120px" width="18" height="32" viewBox="0 0 18 32"><path d="M2 2l14 14L2 30" stroke="#333" stroke-width="1.6" fill="none"/></svg>

  <div class="room" style="left:105px"><div class="pic" role="img" aria-label="Studio room" style="background:linear-gradient(180deg,#c9a06a,#8a5a2a 55%,#e2c9c9)"></div><h3>Studio</h3><p>Lorem ipsum dolor sit amet, constetur adipiscing elit, sed do eiusmod</p><div class="rate">per night +highlight size sq.m.</div><div class="more">View more <svg width="14" height="14" viewBox="0 0 16 16"><circle cx="8" cy="8" r="8" fill="#990a35"/><path d="M6.5 4.5L10 8l-3.5 3.5" stroke="#fff" stroke-width="2" fill="none"/></svg></div></div>
  <div class="room" style="left:355px"><div class="pic" role="img" aria-label="A1 apartment with terrace" style="background:linear-gradient(180deg,#6a8a4a,#a9b98a 45%,#7a5a3a)"></div><h3>A1</h3><p>Lorem ipsum dolor sit amet, constetur adipiscing elit, sed do eiusmod</p><div class="rate">per night +highlight size sq.m.</div><div class="more">View more <svg width="14" height="14" viewBox="0 0 16 16"><circle cx="8" cy="8" r="8" fill="#990a35"/><path d="M6.5 4.5L10 8l-3.5 3.5" stroke="#fff" stroke-width="2" fill="none"/></svg></div></div>
  <div class="room" style="left:605px"><div class="pic" role="img" aria-label="A2 apartment living room" style="background:linear-gradient(180deg,#d9cfc4,#9a3a2a 55%,#6a2a1a)"></div><h3>A2</h3><p>Lorem ipsum dolor sit amet, constetur adipiscing elit, sed do eiusmod</p><div class="rate">per night +highlight size sq.m.</div><div class="more">View more <svg width="14" height="14" viewBox="0 0 16 16"><circle cx="8" cy="8" r="8" fill="#990a35"/><path d="M6.5 4.5L10 8l-3.5 3.5" stroke="#fff" stroke-width="2" fill="none"/></svg></div></div>
  <div class="room" style="left:855px"><div class="pic" role="img" aria-label="Villa building at dusk" style="background:linear-gradient(180deg,#2a3a6a,#5a6a9a 50%,#1a2a4a)"></div><h3>Villa</h3><p>Lorem ipsum dolor sit amet, constetur adipiscing elit, sed do eiusmod</p><div class="rate">per night +highlight size sq.m.</div><div class="more">View more <svg width="14" height="14" viewBox="0 0 16 16"><circle cx="8" cy="8" r="8" fill="#990a35"/><path d="M6.5 4.5L10 8l-3.5 3.5" stroke="#fff" stroke-width="2" fill="none"/></svg></div></div>
</section>

<footer class="site-footer">
  <div class="brand-mark" style="left:172px;top:75px;width:22px;height:22px"></div>
  <div class="brand-name" style="left:112px;top:110px;font-size:30px">Amberline<br>Resort</div>
  <div class="fcol" style="left:354px"><h4>QUICK LINKS</h4>Contact<br>Prices<br>Awards<br>Company details<br>Hotel Fact Sheet</div>
  <div class="fcol" style="left:509px;top:112px">Brochur<br>360® VR<br>Stay Safe Organizer<br>FAQ</div>
  <div class="fcol fcontact" style="left:700px;width:260px"><h4>CONTACT</h4>
    <div><svg width="14" height="18" viewBox="0 0 24 30" style="margin-top:6px"><path d="M12 0a10 10 0 0 0-10 10c0 8 10 20 10 20s10-12 10-20A10 10 0 0 0 12 0zm0 14a4 4 0 1 1 0-8 4 4 0 0 1 0 8z" fill="#fff"/></svg><span style="line-height:22px;padding-top:3px">1234 Somestreet Anywhere<br>USA 21212</span></div>
    <div><svg width="14" height="14" viewBox="0 0 24 24" fill="#fff" style="margin-top:7px"><path d="M6.6 10.8a15 15 0 0 0 6.6 6.6l2.2-2.2a1 1 0 0 1 1-.25 11.4 11.4 0 0 0 3.6.57 1 1 0 0 1 1 1V20a1 1 0 0 1-1 1A17 17 0 0 1 3 4a1 1 0 0 1 1-1h3.5a1 1 0 0 1 1 1c0 1.25.2 2.45.57 3.6a1 1 0 0 1-.25 1z"/></svg>888 - 888 - 8888</div>
    <div><svg width="16" height="12" viewBox="0 0 16 12" style="margin-top:9px"><rect x="0.5" y="0.5" width="15" height="11" fill="none" stroke="#fff"/><path d="M1 1l7 6 7-6" stroke="#fff" fill="none"/></svg>info@amberlineresort.com</div>
  </div>
  <div class="fcol" style="left:995px"><h4>MORE</h4>Terms<br>Disclaimer<br>Privacy Policy</div>
  <div class="frule"></div>
  <div class="copy">© 2021Amberline Resort. All Rights Reserved</div>
  <div class="social" style="left:988px"></div>
  <div class="social" style="left:1024px"></div>
  <div class="social" style="left:1060px"></div>
</footer>

</body>
</html>
```